Investment Fund Investor newsletter

I deleted the tear sheet example which was provided for design purposes only and not for content. Please see the simple outline for the newsletter and the related sections.

Please be clear this project is for a newsletter template. This means a template that can be updated on a monthly or quarterly basis with new content for our audience. Sections should include: Operations Update, Financial Update, Energy Investor News.

We need a template for a newsletter that can be sent out in Word format and also able to send out via Mailchimp. Audience are current investors in our oil and gas fund. These investors are high net worth individuals and private equity firms so the branding needs to be high end, sophisticated and corporate. Please see website and attached tear sheet for the type of branding that we want to match. Website is www.brambleford-power.com
Please see website and tear sheet for the color scheme that we want.

Target Market(s)

Our current fund investors that include high net worth investors and CEOs of private equity companies

Industry/Entity Type

oil and gas... investment

Font styles to use
Serif

Requirements
Must have
• Word file and can send via Mailchimp too

```html
<!DOCTYPE html>
<html lang="en">
<head>
<meta charset="utf-8">
<title>Brambleford Energy Partners – Investor Newsletter</title>
<link rel="stylesheet" href="https://fonts.googleapis.com/css2?family=Barlow:wght@700;800&family=Mulish:wght@400;500;600&family=Roboto+Condensed:wght@400&display=swap">
<style>
  :root {
    --brand-blue: #1a6ea6;
    --brand-blue-deep: #135a8c;
    --brand-blue-light: #4a93c4;
    --accent-blue: #1f7bb8;
    --ink: #111111;
    --ink-soft: #333333;
    --divider: #c9c9c9;
    --paper: #ffffff;
  }
  * { box-sizing: border-box; margin: 0; padding: 0; }
  html, body { width: 936px; height: 1200px; overflow: hidden; background: var(--paper); }
  body { position: relative; font-family: "Mulish", sans-serif; color: var(--ink); }

  .masthead { position: absolute; left: 0; top: 0; width: 568px; height: 782px;
    background: linear-gradient(180deg, #ffffff 0%, #f6f6f6 40%, #e9e9e9 100%); }
  .brand { position: absolute; left: 52px; top: 78px; display: flex; align-items: center; gap: 14px; }
  .brand-mark { width: 34px; height: 34px; background: var(--ink); }
  .brand-name { font-family: "Mulish", sans-serif; font-weight: 600; font-size: 24px; line-height: 1.15; color: var(--ink); letter-spacing: 1px; }
  .tagline { position: absolute; left: 47px; top: 220px; font-size: 24.5px; font-weight: 500; line-height: 46px; color: var(--ink); }
  .tagline .highlight { color: var(--accent-blue); }
  .hero-photo { position: absolute; left: 0; top: 318px; width: 568px; height: 464px;
    background:
      radial-gradient(ellipse 140px 120px at 370px 250px, rgba(240,150,80,0.55), rgba(240,150,80,0) 70%),
      radial-gradient(ellipse 230px 260px at 380px 230px, rgba(120,110,105,0.45), rgba(120,110,105,0) 75%),
      linear-gradient(180deg, rgba(255,255,255,0) 0%, rgba(200,200,200,0.55) 45%, rgba(175,175,175,0.75) 100%); }

  .intro { position: absolute; left: 47px; top: 826px; width: 522px; font-size: 14.5px; line-height: 22px; color: var(--ink-soft); }

  .partners { position: absolute; left: 30px; top: 942px; width: 530px; }
  .partner-row { display: flex; align-items: center; justify-content: center; height: 46px; }
  .partner-row + .partner-row { margin-top: 14px; }
  .partner { padding: 0 14px; font-size: 14px; font-weight: 500; color: var(--brand-blue-deep); white-space: nowrap; }
  .partner.small { font-size: 11px; line-height: 13px; white-space: normal; width: 130px; }
  .partner-sep { width: 1px; height: 38px; background: var(--divider); }

  .footer-band { position: absolute; left: 0; top: 1050px; width: 568px; height: 74px; background: var(--brand-blue);
    color: #fff; text-align: center; font-size: 15px; line-height: 27px; padding-top: 10px; }

  .copyright { position: absolute; left: 0; top: 1166px; width: 936px; padding-left: 262px; font-size: 14.5px; color: var(--ink); }

  .top-block { position: absolute; left: 599px; top: 0; width: 337px; height: 91px; background: var(--brand-blue); }

  .update-card { position: absolute; left: 599px; width: 337px; color: #fff; text-align: center; overflow: hidden; }
  .card-photo { position: absolute; inset: 0; }
  .card-content { position: relative; padding: 24px 20px 0 20px; }
  .card-title { font-family: "Barlow", sans-serif; font-weight: 800; font-size: 31px; line-height: 38px; letter-spacing: 0.3px; margin-bottom: 12px; }
  .card-body { font-family: "Roboto Condensed", sans-serif; font-size: 18.5px; line-height: 29.5px; text-align: justify; text-align-last: center; }

  .card-operations { top: 118px; height: 312px; }
  .card-operations .card-photo { background: linear-gradient(160deg, #2a78ad 0%, #1b6aa1 50%, #2c7cb0 100%); }
  .card-financial { top: 462px; height: 312px; }
  .card-financial .card-photo { background: linear-gradient(170deg, #1c6ca3 0%, #2b7bb0 55%, #5a9bc8 100%); }
  .card-financial .card-content { padding-top: 38px; }
  .card-news { top: 812px; height: 312px; }
  .card-news .card-photo { background: linear-gradient(165deg, #1e6fa6 0%, #236f9f 50%, #1a6396 100%); }
</style>
</head>
<body>
  <section class="masthead">
    <div class="brand">
      <span class="brand-mark"></span>
      <span class="brand-name">BRAMBLEFORD<br>ENERGY PARTNERS</span>
    </div>
    <h1 class="tagline">Consolidating West Texas Conventional<br><span class="highlight">Oil &amp; Gas Assets</span> Into A High Return Fund</h1>
    <div class="hero-photo" role="img" aria-label="Photo of an engineer in a hard hat blended with an oil refinery skyline"></div>
  </section>

  <p class="intro">Lorem Ipsum is simply dummy text of the printing and typesetting industry. Lorem Ipsum has been the industry's standard dummy text ever since the 1500s, when an unknown printer took a galley of type and scrambled it to make a type specimen book.</p>

  <div class="partners">
    <div class="partner-row">
      <span class="partner">Halvard Crest</span>
      <span class="partner-sep"></span>
      <span class="partner small">Ostrander Vale &amp; Pike PC</span>
      <span class="partner-sep"></span>
      <span class="partner">Prairie Commerce Bank</span>
    </div>
    <div class="partner-row">
      <span class="partner">Stonegate Petroleum</span>
      <span class="partner-sep"></span>
      <span class="partner">Kettle Labs</span>
    </div>
  </div>

  <footer class="footer-band">
    Brambleford Energy Partners:<br>
    2318 W. Cedar Ridge Ave Ste 14 #208, Midland Texas, 79707 | 432-555-0187
  </footer>

  <p class="copyright">© copyrights 2022 Brambleford |&nbsp; All Rights Reserved</p>

  <div class="top-block"></div>

  <article class="update-card card-operations">
    <div class="card-photo" role="img" aria-label="Blue-toned photo of an oil field facility"></div>
    <div class="card-content">
      <h2 class="card-title">OPERATIONS<br>UPDATE</h2>
      <p class="card-body">Lorem Ipsum is simply dummy text of the printing and typesetting industry. Lorem Ipsum has been the industry's standard dummy text ever since the 1500.</p>
    </div>
  </article>

  <article class="update-card card-financial">
    <div class="card-photo" role="img" aria-label="Blue-toned photo of financial reports on a desk"></div>
    <div class="card-content">
      <h2 class="card-title">FINANCIAL UPDATE</h2>
      <p class="card-body">Lorem Ipsum is simply dummy text of the printing and typesetting industry. Lorem Ipsum has been the industry's standard dummy text ever since the 1500.</p>
    </div>
  </article>

  <article class="update-card card-news">
    <div class="card-photo" role="img" aria-label="Blue-toned photo of an energy site worker"></div>
    <div class="card-content">
      <h2 class="card-title">ENERGY INVESTOR<br>NEWS</h2>
      <p class="card-body">Lorem Ipsum is simply dummy text of the printing and typesetting industry. Lorem Ipsum has been the industry's standard dummy text ever since the 1500.</p>
    </div>
  </article>
</body>
</html>
```